a Label for a candle jar and its gift box

I would like a label that is modern minimalist for candles jars. These jars are colored as white, amber and black. I am thinking maybe foiling gold/silver background with logo only and maybe company name in different color that suits the foiling background color/s. I would like a high quality luxurious design that shows the preciousness of this candle. I am open to any ideas you might have for the design but so far I have used a logo only on the jar which I really like BUT I still feel that it is not enough branding for people when you only show them the logo so I am considering adding the business name. Again, I am open to both ideas (with logo only or logo with business name (Velvet Lantern).

IMPORTANT: YOU MAY IGNORE MY DESIGN COMPLETELY AND DO YOUR OWN ONE AS LONG AS YOU KERP THE LOGO DESIGN. YOU MAY ALSO ADJUST THE LOGO A BIT TO SUIT YOUR DESIGN. - sorry im using capital letters to show importance but im not yelling :)
Updates

UPDATE: To clarify, I have uploaded a video called Corvale in the box to show what the current product look like. It is a corvale jar with a logo only and the jar box has a window that shows the jar with the logo on it and the back of that jar box has a bigger version of the label that has more details (i.e. Fragrance name and website link). So to make it clear, I would like to have two versions of the lables: 1. on the jar with minimal info (logo only or logo with the business name) 2. Bigger version of the label with more info to put on the back of the jar box - as described above. The dimensions of the jars are as per this link https://www.plintova.com.au/corvale-medium-base-and-flat-lid-amber-packed-with-lid-on/ The dimensions of the jar box as per this link https://www.plintova.com.au/corvale-medium-flat-lid-candle-box-with-window-beige/ Looking forward to some artistic productions :)

Update #2: Tues 25 Dec 18 1. I have uploaded the photo which has the logo with the name 'Velvet Lantern' below it just for a reference. However, I would like the designer to modify the current font and NOT to use it as the word 'of in the phrase 'Velvet Lantern' does not come out clear enough after printing. 2. I would like the designer NOT to create a design that will require a clear sticker/label for printing. 3. I have attached the photos of my current designs on the jars or the jar box just as a reference but please do NOT just use the same fonts and only change background. I am hoping to see something different and more professional than my own design :) Thank you very much!

Font styles to use
Decorative
Script

Requirements
Must have
• I would like them to fit on the three colors of the jars below - white, amber and black. Below is a link to how the jar looks like https://www.plintova.com.au/candle-making-supplies/candle-jars/corvale-candle-jars/?glassware_colour=415,443,417&glassware_size=268
Nice to have
• I would like to have a modern design which is suitable for both feminine and musculine.
Should not have
• shouldnt have so much writing on it!

```html
<!DOCTYPE html>
<html lang="en">
<head>
<meta charset="utf-8">
<title>Velvet Lantern – Jar and Box Labels</title>
<link rel="stylesheet" href="https://fonts.googleapis.com/css2?family=Kaushan+Script&family=Oswald:wght@400&display=swap">
<style>
  :root {
    --page: #ffffff;
    --label-grey: #dcdcdc;
    --label-shadow: rgba(0, 0, 0, 0.28);
    --glitter-deep: #a9564d;
    --glitter-mid: #c47a6f;
    --glitter-light: rgba(222, 160, 148, 0.55);
    --script-white: #ffffff;
    --script-shadow: rgba(60, 40, 40, 0.45);
    --mark-circle: #e6e6e6;
    --url-ink: #1c1c1c;
  }
  * { box-sizing: border-box; margin: 0; padding: 0; }
  html, body {
    width: 1200px;
    height: 700px;
    overflow: hidden;
    background: var(--page);
  }
  .canvas {
    position: relative;
    width: 1200px;
    height: 700px;
  }
  .label {
    position: absolute;
    width: 560px;
    height: 560px;
    border-radius: 50%;
    background: var(--label-grey);
    box-shadow: 7px 10px 14px var(--label-shadow);
    overflow: hidden;
  }
  .label--jar { left: 36px; top: 60px; }
  .label--box { left: 628px; top: 60px; }

  .glitter-splash {
    position: absolute;
    border-radius: 46% 54% 40% 60% / 55% 45% 55% 45%;
    background:
      radial-gradient(ellipse at 45% 50%,
        var(--glitter-deep) 0%,
        var(--glitter-mid) 40%,
        var(--glitter-light) 62%,
        rgba(222, 160, 148, 0) 74%);
  }
  .label--jar .glitter-splash { left: 70px; top: 110px; width: 420px; height: 350px; }
  .label--box .glitter-splash { left: 60px; top: 125px; width: 450px; height: 340px; }

  .brand-mark {
    position: absolute;
    display: flex;
    align-items: center;
    font-family: "Kaushan Script", cursive;
    color: var(--script-white);
    white-space: nowrap;
  }
  .brand-mark__circle {
    border-radius: 50%;
    background: var(--mark-circle);
    flex: none;
  }
  .label--jar .brand-mark {
    left: 40px; top: 228px;
    font-size: 62px;
    gap: 14px;
  }
  .label--jar .brand-mark__circle { width: 96px; height: 96px; }
  .label--box .brand-mark {
    left: 175px; top: 150px;
    font-size: 30px;
    gap: 8px;
  }
  .label--box .brand-mark__circle { width: 48px; height: 48px; }

  .fragrance-name {
    position: absolute;
    left: 0; width: 100%;
    text-align: center;
    font-family: "Kaushan Script", cursive;
    font-size: 70px;
    line-height: 92px;
    color: var(--script-white);
    text-shadow: 6px 8px 8px var(--script-shadow);
    top: 214px;
  }
  .site-address {
    position: absolute;
    left: 0; width: 100%;
    top: 428px;
    text-align: center;
    font-family: "Oswald", sans-serif;
    font-size: 19px;
    color: var(--url-ink);
  }
</style>
</head>
<body>
<main class="canvas">
  <section class="label label--jar" aria-label="Jar label">
    <div class="glitter-splash" role="img" aria-label="Rose gold glitter splash"></div>
    <div class="brand-mark">
      <span class="brand-mark__name">Velvet Lantern</span>
      <span class="brand-mark__circle"></span>
    </div>
  </section>

  <section class="label label--box" aria-label="Box label">
    <div class="glitter-splash" role="img" aria-label="Rose gold glitter splash"></div>
    <div class="brand-mark">
      <span class="brand-mark__name">Velvet Lantern</span>
      <span class="brand-mark__circle"></span>
    </div>
    <h1 class="fragrance-name">Zesty Tangerine<br>Guava</h1>
    <p class="site-address">www.VelvetLantern.com.au</p>
  </section>
</main>
</body>
</html>
```